Water Bottle Design

We are launching a water bottle and need a impactful design.

Target Market(s)

health conscious hipsters

Font styles to use
Sans Serif

Requirements
Must have
• Please include the logo (included) on one side of the bottle and these words on the other side of the bottle. "It’s simple, REUSE this bottle every day. Your action, will REDUCE the amount of waste produced. SAVE your body from drinking the harmful contaminants in your water from Non-BPA plastics. HELP someone else because proceeds from your purchase will help homeless veterans.
• We’re just two dudes that like to drink water and help people. #PayItFoward"
• Use a total of two colors
• UPDATE: You do not have to use the bottle on the logo.
Nice to have
• The bottle itself is 34 ounces and looks like a normal water bottle. I will include the image in the files. We would need to be able to change the colors easily.
Should not have
• Do not use more than two colors. Colors should not be important to the design at this point.

```html
<!DOCTYPE html>
<html lang="en">
<head>
<meta charset="utf-8">
<title>RVA Bottle Wrap</title>
<link rel="stylesheet" href="https://fonts.googleapis.com/css2?family=Josefin+Sans:wght@300;400;600;700&family=Oswald:wght@400;500&display=swap">
<style>
  :root {
    --bottle-green: #7ad04a;
    --leaf-light: #b9e69c;
    --ink: #111a0c;
    --white: #ffffff;
    --stage: #eef0ec;
  }
  * { box-sizing: border-box; margin: 0; padding: 0; }
  html, body { width: 1200px; height: 1101px; overflow: hidden; }
  body {
    background: var(--stage);
    display: flex;
    align-items: center;
    justify-content: center;
    gap: 44px;
    font-family: "Josefin Sans", Arial, sans-serif;
  }
  .wrap-panel {
    width: 350px;
    height: 1000px;
    background: var(--bottle-green);
    position: relative;
    overflow: hidden;
  }

  /* Front: brand side */
  .brand-lockup {
    position: absolute;
    left: 44px;
    top: 92px;
    display: flex;
    align-items: flex-start;
    gap: 14px;
    color: var(--white);
  }
  .brand-mark-square {
    width: 22px;
    height: 22px;
    background: var(--white);
    margin-top: 14px;
  }
  .brand-name {
    font-weight: 300;
    font-size: 104px;
    line-height: 0.9;
    letter-spacing: 2px;
  }
  .brand-tagline {
    font-size: 15px;
    font-weight: 400;
    letter-spacing: 1px;
    margin-top: 8px;
  }
  .leaf-artwork {
    position: absolute;
    left: 22px;
    top: 350px;
    width: 300px;
    height: 330px;
    border-radius: 50% 50% 50% 50% / 55% 55% 45% 45%;
    background: radial-gradient(circle at 50% 40%, var(--leaf-light), rgba(185,230,156,0.55) 60%, rgba(185,230,156,0) 72%);
  }

  /* Back: message side */
  .message-box {
    position: absolute;
    left: 34px;
    right: 34px;
    top: 40px;
    bottom: 40px;
    border: 3px solid var(--ink);
    color: var(--ink);
    padding: 0 16px 18px;
    text-transform: uppercase;
    display: flex;
    flex-direction: column;
    justify-content: space-between;
  }
  .message-heading {
    font-family: "Oswald", Arial, sans-serif;
    font-weight: 500;
    font-size: 30px;
    letter-spacing: 5px;
    text-align: center;
    border-bottom: 3px solid var(--ink);
    margin: 0 -16px;
    padding: 10px 0 8px;
  }
  .message-block { padding-top: 6px; }
  .message-keyword {
    font-weight: 300;
    font-size: 58px;
    letter-spacing: 8px;
    text-indent: 8px;
    line-height: 1;
    text-align: center;
    border-top: 2px solid var(--ink);
    border-bottom: 2px solid var(--ink);
    padding: 10px 0 2px;
    margin-bottom: 12px;
  }
  .message-copy {
    font-weight: 600;
    font-size: 17px;
    line-height: 1.3;
    letter-spacing: 0.5px;
  }
  .message-copy .emphasis {
    display: block;
    font-size: 26px;
    line-height: 1.15;
    letter-spacing: 1px;
    margin: 2px 0;
  }
  .emphasis-light { font-weight: 300; }
  .emphasis-bold { font-weight: 600; }
  .message-closing {
    font-family: "Oswald", Arial, sans-serif;
    font-weight: 400;
    font-size: 44px;
    letter-spacing: 2px;
    line-height: 1.05;
    margin-top: 2px;
  }
  .message-footer {
    font-weight: 600;
    font-size: 17px;
    letter-spacing: 1px;
    margin-top: 6px;
  }
</style>
</head>
<body>
  <section class="wrap-panel wrap-front">
    <div class="brand-lockup">
      <span class="brand-mark-square"></span>
      <div>
        <div class="brand-name">RVA</div>
        <div class="brand-tagline">Rova Water Co.</div>
      </div>
    </div>
    <div class="leaf-artwork" role="img" aria-label="Light green cluster of leaves forming a water drop"></div>
  </section>

  <section class="wrap-panel wrap-back">
    <div class="message-box">
      <h2 class="message-heading">It's Simple</h2>

      <div class="message-block">
        <div class="message-keyword">Reuse</div>
        <p class="message-copy">This bottle every day. Your action will reduce the amount of waste produced.</p>
      </div>

      <div class="message-block">
        <div class="message-keyword">Save</div>
        <p class="message-copy">Our body from drinking
          <span class="emphasis emphasis-light">The harmful</span>
          <span class="emphasis emphasis-bold">Contaminants</span>
          in your water from Non-BPA plastics</p>
      </div>

      <div class="message-block">
        <div class="message-keyword">Help</div>
        <p class="message-copy">Someone else because proceeds from
          <span class="emphasis emphasis-light">Your purchase</span></p>
        <div class="message-closing">Will Help</div>
        <p class="message-footer">Homeless veterans</p>
      </div>
    </div>
  </section>
</body>
</html>
```